Surviving Domestic Violence Flyer

I need a flyer that "POPS" to attract participants for my research project. I have added the important information on my draft flyer.

```html
<!DOCTYPE html>
<html lang="en">
<head>
<meta charset="utf-8">
<title>Request for Study Participants – Survivor Resources Study</title>
<link rel="stylesheet" href="https://fonts.googleapis.com/css2?family=Oswald:wght@500;700&family=Arimo:wght@700&family=Roboto+Condensed:wght@700&display=swap">
<style>
  :root {
    --red: #e3191f;
    --red-deep: #8e0b0f;
    --black: #000000;
    --white: #ffffff;
    --yellow: #f7e43c;
    --label-red: #ea2a2f;
    --tab-red: #e0161c;
  }
  * { box-sizing: border-box; margin: 0; padding: 0; }
  html, body { width: 926px; height: 1200px; overflow: hidden; background: var(--white); }
  .flyer { position: relative; width: 926px; height: 1200px; background: var(--black); font-family: "Arimo", Arial, sans-serif; }

  .hero {
    position: absolute; left: 0; top: 0; width: 926px; height: 614px;
    background:
      radial-gradient(ellipse 420px 460px at 250px 230px, #f0363b 0%, rgba(240,54,59,0) 70%),
      linear-gradient(90deg, #b80f14 0%, var(--red) 40%, #d01519 72%, #3a0406 100%);
  }
  .hero::after {
    content: ""; position: absolute; inset: 0;
    background: linear-gradient(180deg, rgba(0,0,0,0) 55%, rgba(60,0,2,0.55) 100%);
  }
  .headline {
    position: absolute; right: 40px; top: 22px; z-index: 1;
    font-family: "Oswald", "Arial Narrow", sans-serif; font-weight: 700;
    color: var(--white); font-size: 58px; line-height: 74px; text-align: right; letter-spacing: 0.5px;
  }
  .study-title {
    position: absolute; left: 55px; top: 432px; z-index: 1;
    font-family: "Oswald", "Arial Narrow", sans-serif; font-weight: 700;
    color: var(--white); font-size: 46px; line-height: 56px; text-transform: uppercase; letter-spacing: 0.3px;
  }
  .compensation {
    position: absolute; left: 723px; top: 518px; z-index: 1;
    color: var(--white); font-size: 17px; line-height: 25px; letter-spacing: 0.4px;
  }
  .divider { position: absolute; left: 0; top: 614px; width: 926px; height: 3px; background: var(--white); }

  .criteria {
    position: absolute; left: 58px; top: 636px; list-style: none;
    color: var(--yellow); font-size: 20.5px; line-height: 28px; letter-spacing: 0.5px;
  }
  .criteria li { padding-left: 18px; text-indent: -18px; }
  .criteria li::before { content: "•"; display: inline-block; width: 18px; text-indent: 0; }

  .invitation {
    position: absolute; left: 55px; top: 841px; width: 510px;
    color: var(--white); font-size: 16.5px; line-height: 22px; letter-spacing: 0.3px;
  }
  .invitation p + p { margin-top: 14px; }

  .study-details {
    position: absolute; left: 572px; top: 842px; width: 330px;
    font-family: "Roboto Condensed", "Arial Narrow", sans-serif; font-size: 16.5px; line-height: 21px; color: var(--white);
  }
  .study-details p + p { margin-top: 7px; }
  .study-details .label { color: var(--label-red); }

  .tear-strip {
    position: absolute; left: 0; top: 1029px; width: 926px; height: 171px;
    display: flex; background: var(--white); border-top: 1px solid #999;
  }
  .tab {
    flex: 1; border-left: 1px solid #9a9a9a;
    display: flex; justify-content: center; align-items: center;
  }
  .tab:first-child { border-left: none; }
  .tab-text {
    writing-mode: vertical-rl; transform: rotate(180deg);
    font-family: "Roboto Condensed", "Arial Narrow", sans-serif; white-space: nowrap;
    display: flex; flex-direction: column; align-items: flex-start;
  }
  .tab-study { color: var(--black); font-size: 11.5px; line-height: 16px; }
  .tab-phone { color: var(--tab-red); font-size: 17px; line-height: 20px; }
</style>
</head>
<body>
<main class="flyer">
  <section class="hero" role="img" aria-label="Red-tinted photograph of a distressed woman sitting against a wall, hugging her arms"></section>
  <h1 class="headline">Request for<br>Study Participants</h1>
  <h2 class="study-title">Efficiency of resources<br>available to survivors<br>of intimate partner abuse</h2>
  <p class="compensation">Participants will<br>be compensated<br>for their time</p>
  <div class="divider"></div>

  <ul class="criteria">
    <li>Are you eighteen years of age older?</li>
    <li>Have you been a victim of domestic violence?</li>
    <li>Have you sought assistance with abuse in the last 12 months?</li>
    <li>Are you still in contact with a person who abused you?</li>
    <li>Are you willing and open to discussing your experience with abuse and your attempts to access services or resources?</li>
  </ul>

  <div class="invitation">
    <p>If you answered yes to all of these questions, you may be eligible to participate in a study to better understand the resources needed and services expected for survivors of domestic violence.</p>
    <p>Please contact Dana Whitfield at 1(555)214-0386 or via e-mail survivorstudy@examplemail.com for additional information.</p>
  </div>

  <div class="study-details">
    <p><span class="label">PRINCIPAL INVESTIGATOR:</span> Dana Whitfield</p>
    <p><span class="label">INSTITUTIONAL AFFILIATION:</span> Lakeshore State University, Dept. of Criminology, Law and Jusice</p>
    <p><span class="label">CONTACT ADDRESS:</span> Post Office Box 204518, Riverton, IL, 60999</p>
  </div>

  <div class="tear-strip">
    <div class="tab"><div class="tab-text"><span class="tab-study">Survivor Resources Study</span><span class="tab-phone">1(555)214-0386</span></div></div>
    <div class="tab"><div class="tab-text"><span class="tab-study">Survivor Resources Study</span><span class="tab-phone">1(555)214-0386</span></div></div>
    <div class="tab"><div class="tab-text"><span class="tab-study">Survivor Resources Study</span><span class="tab-phone">1(555)214-0386</span></div></div>
    <div class="tab"><div class="tab-text"><span class="tab-study">Survivor Resources Study</span><span class="tab-phone">1(555)214-0386</span></div></div>
    <div class="tab"><div class="tab-text"><span class="tab-study">Survivor Resources Study</span><span class="tab-phone">1(555)214-0386</span></div></div>
    <div class="tab"><div class="tab-text"><span class="tab-study">Survivor Resources Study</span><span class="tab-phone">1(555)214-0386</span></div></div>
    <div class="tab"><div class="tab-text"><span class="tab-study">Survivor Resources Study</span><span class="tab-phone">1(555)214-0386</span></div></div>
    <div class="tab"><div class="tab-text"><span class="tab-study">Survivor Resources Study</span><span class="tab-phone">1(555)214-0386</span></div></div>
    <div class="tab"><div class="tab-text"><span class="tab-study">Survivor Resources Study</span><span class="tab-phone">1(555)214-0386</span></div></div>
    <div class="tab"><div class="tab-text"><span class="tab-study">Survivor Resources Study</span><span class="tab-phone">1(555)214-0386</span></div></div>
    <div class="tab"><div class="tab-text"><span class="tab-study">Survivor Resources Study</span><span class="tab-phone">1(555)214-0386</span></div></div>
    <div class="tab"><div class="tab-text"><span class="tab-study">Survivor Resources Study</span><span class="tab-phone">1(555)214-0386</span></div></div>
    <div class="tab"><div class="tab-text"><span class="tab-study">Survivor Resources Study</span><span class="tab-phone">1(555)214-0386</span></div></div>
    <div class="tab"><div class="tab-text"><span class="tab-study">Survivor Resources Study</span><span class="tab-phone">1(555)214-0386</span></div></div>
  </div>
</main>
</body>
</html>
```